Successful Software Co Launching A Super FUN Mobile & Web Application - ROCKSTAR Designer Needed

Our App is called "Brightly Tally"It is an employee "gamification" app designed to make working at your job fun...Employees complete simple tasks throughout the work day and are rewarded with points they can redeem for different gifts and benefits...We an AMAZING User Interface designed for both the mobile app and website app. We are looking for a clean, modern and simple design... This app is designed to make employees more engaged at work while having fun doing the things they already do each day...They can then redeem their points for rewards. It needs to be easy to understand and simple in its design...Example: A local carpet cleaning business uses our app.Their employees show up to work on time - They get 50 pointsThey clean out their work vehicle - They get 100 pointsThey up-sell an additional cleaning job - The get 250 pointsEtc...The app will also have fun icons and graphics that appear on the screen when an employee accomplishes a task.The app will play fun music sounds when they accomplish tasks too.
Updates

Need extra days to review

Target Market(s)

Small business owners

Logo Text

Brightly Tally

Font styles to use
Sans Serif

Colors

Designer to choose colors to be used in the design.

Requirements
Must have
• Simple elegant design
Nice to have
• I'd like to see examples of fun "icons" that could pop up on the screen after an employee completes a "task" and earns points... Something fun to pop up on the screen... (like a happy face, a thumbs up, fun text bubbles... "Way To Go!" etc... or any other fun ideas)

```html
<!DOCTYPE html>
<html lang="en">
<head>
<meta charset="utf-8">
<title>Brightly Tally – Employee Rewards Home</title>
<link href="https://fonts.googleapis.com/css2?family=Pacifico&display=swap" rel="stylesheet">
<style>
  :root {
    --page-bg: #ffffff;
    --ink-light: #ffffff;
    --ink-dark: #1c1a14;
    --accent-yellow: #fdbd00;
    --accent-red: #922523;
    --button-dark: #262824;
    --glass: rgba(255, 255, 255, 0.22);
    --card-glass: rgba(95, 95, 90, 0.55);
    --divider: rgba(255, 255, 255, 0.18);
  }
  * { box-sizing: border-box; margin: 0; padding: 0; }
  html, body {
    width: 1200px; height: 1200px; overflow: hidden;
    background: var(--page-bg);
    font-family: "Pacifico", cursive;
  }
  .app-screen {
    position: absolute; left: 318px; top: 66px;
    width: 564px; height: 1068px; overflow: hidden;
    color: var(--ink-light);
  }
  .hero-backdrop {
    position: absolute; inset: 0;
    background:
      radial-gradient(ellipse at 30% 40%, rgba(120,125,150,0.55), transparent 55%),
      radial-gradient(ellipse at 75% 30%, rgba(150,140,60,0.6), transparent 60%),
      linear-gradient(180deg, #7d7a45 0%, #6f6a3c 30%, #5e5a36 55%, #3a3a28 78%, #181a14 100%);
  }
  .top-bar { position: absolute; top: 95px; left: 60px; right: 54px; height: 26px; }
  .menu-icon { position: absolute; left: 0; top: 0; }
  .settings-icon { position: absolute; right: 0; top: -2px; }
  .welcome-title {
    position: absolute; top: 138px; left: 0; right: 0;
    text-align: center; font-size: 34px; line-height: 50px; font-weight: 400;
  }
  .progress-pill {
    position: absolute; left: 47px; top: 290px; width: 491px; height: 54px;
    border-radius: 27px; background: var(--glass);
    display: flex; align-items: center; justify-content: center;
    font-size: 16px;
  }
  .monthly-goal {
    position: absolute; top: 352px; left: 0; right: 0;
    text-align: center; font-size: 27px;
  }
  .redeem-button {
    position: absolute; left: 146px; top: 422px; width: 291px; height: 66px;
    border-radius: 33px; background: var(--accent-yellow); color: var(--ink-dark);
    display: flex; align-items: center; justify-content: center; font-size: 22px;
  }
  .history-heading {
    position: absolute; top: 500px; left: 0; right: 0;
    text-align: center; font-size: 23px;
  }
  .history-card {
    position: absolute; left: 35px; top: 555px; width: 494px; height: 402px;
    border-radius: 28px; background: var(--card-glass);
  }
  .history-row {
    position: absolute; left: 18px; right: 15px;
    display: flex; align-items: center; justify-content: space-between;
  }
  .history-row + .history-row::before { content: none; }
  .row-label { font-size: 17px; line-height: 24px; max-width: 300px; }
  .points-badge {
    width: 112px; height: 46px; border-radius: 23px; flex: none;
    background: var(--accent-yellow); color: var(--ink-dark);
    display: flex; align-items: center; justify-content: center; font-size: 17px;
  }
  .row-divider {
    position: absolute; left: 18px; width: 461px; height: 1px; background: var(--divider);
  }
  .action-button {
    position: absolute; top: 998px; width: 234px; height: 90px;
    border-radius: 28px 28px 0 0; padding-bottom: 20px;
    display: flex; align-items: center; justify-content: center; font-size: 25px;
  }
  .contact-employer { left: 50px; background: var(--accent-red); }
  .request-time-off { left: 291px; background: var(--button-dark); }
</style>
</head>
<body>
<main class="app-screen">
  <div class="hero-backdrop" role="img" aria-label="Blurred photo of a worker in a cap and overalls working outdoors among greenery"></div>

  <header class="top-bar">
    <svg class="menu-icon" width="26" height="20" viewBox="0 0 26 20" aria-label="Menu">
      <g stroke="#fff" stroke-width="1.5" stroke-linecap="round">
        <line x1="4" y1="1" x2="25" y2="1"/>
        <line x1="1" y1="10" x2="25" y2="10"/>
        <line x1="4" y1="19" x2="25" y2="19"/>
      </g>
    </svg>
    <svg class="settings-icon" width="28" height="28" viewBox="0 0 28 28" aria-label="Settings">
      <g fill="none" stroke="#fff" stroke-width="1.3">
        <path d="M12 2h4l.7 3.3 2.4 1 2.8-1.9 2.8 2.8-1.9 2.8 1 2.4L27 12v4l-3.3.7-1 2.4 1.9 2.8-2.8 2.8-2.8-1.9-2.4 1L16 27h-4l-.7-3.3-2.4-1-2.8 1.9-2.8-2.8 1.9-2.8-1-2.4L1 16v-4l3.3-.7 1-2.4-1.9-2.8 2.8-2.8 2.8 1.9 2.4-1z"/>
        <circle cx="14" cy="14" r="4.5"/>
      </g>
    </svg>
  </header>

  <h1 class="welcome-title">Welcome to Brightly Tally,<br>Dana</h1>

  <p class="progress-pill">you are only 750 points away from your Next Reward</p>

  <p class="monthly-goal">Monthly Goal: 3000 Points</p>

  <a class="redeem-button">Redeem Your Rewards</a>

  <h2 class="history-heading">Reward History</h2>

  <section class="history-card">
    <div class="history-row" style="top:34px">
      <span class="row-label" style="max-width:340px">Show Up On Time Every Day For 1 Month</span>
      <span class="points-badge">100 Points</span>
    </div>
    <div class="row-divider" style="top:101px"></div>
    <div class="history-row" style="top:123px">
      <span class="row-label">Up-Sell over $ 250 In Services</span>
      <span class="points-badge">250 Points</span>
    </div>
    <div class="row-divider" style="top:190px"></div>
    <div class="history-row" style="top:217px">
      <span class="row-label">Pass Your Vehicle Inspection Report Each Week</span>
      <span class="points-badge">250 Points</span>
    </div>
    <div class="row-divider" style="top:286px"></div>
    <div class="history-row" style="top:307px; left:13px; right:19px">
      <span class="row-label">Daily Paperwork Turned In Complete &amp; On Time</span>
      <span class="points-badge">250 Points</span>
    </div>
  </section>

  <a class="action-button contact-employer">Contact Employer</a>
  <a class="action-button request-time-off">Request Time Off</a>
</main>
</body>
</html>
```